Meadow Paws Label

We have basically a start up business that I need help with. This project is just for the label design.

Our product is a frozen raw pet food that promotes weight control, less shedding, smaller stools and an overall better health. The product is in nugget form similar to what you would see in a steak shish kabob. I only share that with you in case you want to incorporate that in the design.

We have been in business for 17 years but all of our sales have been word of mouth. We are going to be launching an infomercial this summer and I need everything stated previously to be completed before we can launch the infomercial.

We need a label created for our first frozen dog food produce. We need the label to say Meadow Paws of course. The label also needs to have the following:

The label needs to be 4 inches x 6 inches.

Combination Diet - Large Font
Ingredients: Beef hearts, beef kidneys, beef tripe, beef liver, chicken necks, chicken mdm, breed premix, broccoli, bone meal, apples, carrots, oystershell, cod liver oil

DATE PACKED: XXXX
LOT #XXXX

BEST IF USED BY: XX-XX-XX

KEEP FROZEN

NET WT. 5 LBS.

```html
<!DOCTYPE html>
<html lang="en">
<head>
<meta charset="UTF-8">
<title>Meadow Paws Label – Combination Diet</title>
<link rel="stylesheet" href="https://fonts.googleapis.com/css2?family=Open+Sans:wght@300;400;700;800&family=Open+Sans+Condensed:wght@700&family=PT+Sans+Narrow:wght@400;700&display=swap">
<style>
  :root {
    --page: #ffffff;
    --label-border: #3a3a3a;
    --orange: #f39020;
    --brown: #773611;
    --brown-text: #7a3a12;
    --ink: #111111;
    --white: #ffffff;
  }
  * { margin: 0; padding: 0; box-sizing: border-box; }
  html, body {
    width: 1200px; height: 1000px; overflow: hidden;
    background: var(--page);
  }
  .label {
    position: absolute; left: 380px; top: 141px;
    width: 488px; height: 732px;
    border: 1px solid var(--label-border);
    background: var(--white);
    overflow: hidden;
  }
  .brand {
    position: absolute; left: 0; top: 60px; width: 100%;
    text-align: center;
  }
  .brand-name {
    display: inline-flex; align-items: center; gap: 14px;
    font-family: "Open Sans", sans-serif; font-weight: 800;
    font-size: 52px; color: var(--ink); letter-spacing: -1px;
    line-height: 1;
  }
  .brand-mark {
    width: 30px; height: 30px; border-radius: 50%;
    background: var(--orange);
  }
  .brand-tagline {
    margin-top: 40px;
    font-family: "Open Sans", sans-serif; font-weight: 700;
    font-size: 13px; letter-spacing: 2px; color: var(--ink);
  }
  .product-band {
    position: absolute; left: 0; top: 281px; width: 100%; height: 350px;
    background: var(--orange);
  }
  .product-title {
    position: absolute; left: 0; top: 24px; width: 100%;
    text-align: center;
    font-family: "Open Sans", sans-serif; font-weight: 800;
    font-size: 62px; color: var(--white); letter-spacing: 1px;
    line-height: 1;
  }
  .subtitle-bar {
    position: absolute; left: 0; top: 140px; width: 100%; height: 42px;
    background: var(--brown);
  }
  .subtitle {
    position: absolute; left: 53px; top: 9px;
    font-family: "Open Sans", sans-serif; font-weight: 300;
    font-size: 18px; color: var(--white); letter-spacing: 2px;
  }
  .subtitle strong { font-weight: 700; }
  .diet-badge {
    position: absolute; left: 313px; top: 86px;
    width: 144px; height: 76px; border-radius: 50%;
    background: var(--white);
    display: flex; align-items: center; justify-content: center;
    font-family: "Open Sans", sans-serif; font-weight: 800;
    font-size: 40px; color: var(--orange); line-height: 1;
  }
  .ingredients {
    position: absolute; left: 49px; top: 258px; width: 400px;
    font-family: "PT Sans Narrow", sans-serif; font-size: 16.5px;
    line-height: 20.5px; color: var(--brown-text);
  }
  .ingredients strong { font-weight: 700; }
  .footer {
    position: absolute; left: 0; top: 636px; width: 100%; height: 96px;
    background: var(--brown);
    color: var(--white); text-align: center;
    font-family: "Open Sans Condensed", "PT Sans Narrow", sans-serif;
    font-weight: 700; font-size: 11px; letter-spacing: 0.2px;
  }
  .footer p { position: absolute; left: 0; width: 100%; }
  .footer .packed { top: 14px; }
  .footer .use-by { top: 32px; }
  .footer .use-by span + span { margin-left: 26px; }
  .footer .net-wt { top: 61px; }
</style>
</head>
<body>
  <div class="label">
    <header class="brand">
      <div class="brand-name"><span class="brand-mark"></span>Meadow Paws</div>
      <div class="brand-tagline">100% NATURAL RAW DOG FOOD</div>
    </header>

    <section class="product-band">
      <h1 class="product-title">COMBINATION</h1>
      <div class="subtitle-bar">
        <p class="subtitle">ALL NATURAL <strong>DOG FOOD</strong></p>
      </div>
      <div class="diet-badge">DIET</div>
      <p class="ingredients"><strong>Ingredients:</strong> Beef hearts, beef kidneys, beef tripe, beef liver, chicken necks, chicken mdm, breed premix, broccoli, bone meal, apples, carrots, oystershell, cod liver oil</p>
    </section>

    <footer class="footer">
      <p class="packed">DATE PACKED: XXXX LOT #XXXX</p>
      <p class="use-by"><span>BEST IF USED BY: XX-XX-XX</span><span>KEEP FROZEN</span></p>
      <p class="net-wt">NET WT. 5 LBS.</p>
    </footer>
  </div>
</body>
</html>
```